Super Global Luxury Business Cards!!!

I need a luxury business card design for a realtor that specializes in luxury homes

Industry/Entity Type

Real Estate

Contact Information for Business Card

a nice luxury design that will make people go WOW this is a NICE card

Requirements
Must have
• my name, phone, email, social media - address - use of both logos

```html
<!DOCTYPE html>
<html lang="en">
<head>
<meta charset="utf-8">
<title>Mr. Vela — Business Card</title>
<link href="https://fonts.googleapis.com/css2?family=Montserrat:wght@400;500;700;800&display=swap" rel="stylesheet">
<style>
  :root {
    --bg: #e9e9e9;
    --ink: #0b0b0b;
    --paper: #ffffff;
    --silver: #d4d4d4;
    --muted: #9a9a9a;
  }
  * { margin: 0; padding: 0; box-sizing: border-box; }
  html, body { width: 1200px; height: 808px; overflow: hidden; }
  body {
    background: var(--bg);
    font-family: "Montserrat", sans-serif;
    display: flex;
    flex-direction: column;
    align-items: center;
    justify-content: center;
    gap: 36px;
  }
  .card {
    width: 640px;
    height: 366px;
    position: relative;
    overflow: hidden;
    box-shadow: 0 6px 18px rgba(0,0,0,.18);
  }

  /* Brand name placeholder: plain text with one small circle beside it */
  .brand-name {
    display: flex;
    align-items: center;
    font-weight: 700;
    letter-spacing: .16em;
    white-space: nowrap;
    line-height: 1;
  }
  .brand-dot {
    border-radius: 50%;
    flex-shrink: 0;
  }

  /* Front */
  .card-front {
    background: radial-gradient(ellipse at 50% 45%, #2e2e2e 0%, #141414 55%, var(--ink) 100%);
    display: flex;
    align-items: center;
    justify-content: center;
  }
  .card-front .brand-name { color: var(--silver); font-size: 34px; gap: 16px; }
  .card-front .brand-dot { width: 18px; height: 18px; background: var(--silver); }

  /* Back */
  .card-back { background: var(--paper); }
  .back-band {
    height: 50%;
    background: var(--ink);
    position: relative;
    padding: 40px 0 0 64px;
    color: var(--paper);
  }
  .person-name {
    font-size: 30px;
    font-weight: 800;
    letter-spacing: .01em;
    line-height: 1;
  }
  .person-title {
    font-size: 15px;
    font-weight: 400;
    color: var(--muted);
    margin-top: 4px;
  }
  .partner {
    position: absolute;
    right: 56px;
    bottom: 14px;
    display: flex;
    flex-direction: column;
    align-items: center;
    gap: 8px;
  }
  .partner-badge {
    width: 50px;
    height: 50px;
    border-radius: 50%;
    border: 2px solid var(--paper);
  }
  .partner-name {
    font-size: 12px;
    font-weight: 700;
    letter-spacing: .04em;
    text-align: center;
    line-height: 1.3;
  }
  .back-body {
    height: 50%;
    display: flex;
    align-items: center;
    padding-left: 48px;
  }
  .card-back .brand-name { color: var(--ink); font-size: 20px; gap: 9px; width: 150px; }
  .card-back .brand-dot { width: 12px; height: 12px; background: var(--ink); }
  .divider {
    width: 1.5px;
    height: 110px;
    background: var(--ink);
    margin: 0 22px 0 18px;
    flex-shrink: 0;
  }
  .contact { list-style: none; color: var(--ink); font-size: 15.5px; font-weight: 500; line-height: 1.55; }
  .contact li { display: flex; align-items: center; gap: 9px; white-space: nowrap; }
  .contact svg { width: 14px; height: 14px; fill: var(--ink); flex-shrink: 0; }
</style>
</head>
<body>

  <section class="card card-front">
    <div class="brand-name"><span class="brand-dot"></span>MR. VELA</div>
  </section>

  <section class="card card-back">
    <div class="back-band">
      <h1 class="person-name">YOUR NAME</h1>
      <p class="person-title">Your Tittle</p>
      <div class="partner">
        <div class="partner-badge"></div>
        <div class="partner-name">HARBORLINE<br>REALTY</div>
      </div>
    </div>
    <div class="back-body">
      <div class="brand-name"><span class="brand-dot"></span>MR. VELA</div>
      <div class="divider"></div>
      <ul class="contact">
        <li>
          <svg viewBox="0 0 24 24"><path d="M6.6 10.8a15.1 15.1 0 0 0 6.6 6.6l2.2-2.2a1 1 0 0 1 1-.25 11.4 11.4 0 0 0 3.6.57 1 1 0 0 1 1 1V20a1 1 0 0 1-1 1A17 17 0 0 1 3 4a1 1 0 0 1 1-1h3.5a1 1 0 0 1 1 1c0 1.25.2 2.45.57 3.57a1 1 0 0 1-.25 1z"/></svg>
          012 345 6789 | Fax 012 345 6789
        </li>
        <li>
          <svg viewBox="0 0 24 24"><path d="M2 5h20v14H2z M3.5 6.5 12 13l8.5-6.5" fill="none" stroke="#0b0b0b" stroke-width="2"/></svg>
          Yourmail@mailbox.com
        </li>
        <li>
          <svg viewBox="0 0 24 24"><g fill="none" stroke="#0b0b0b" stroke-width="2"><circle cx="12" cy="12" r="9"/><path d="M3 12h18M12 3c3 3 3 15 0 18M12 3c-3 3-3 15 0 18"/></g></svg>
          www.yourwebsite.com
        </li>
        <li>Street Address Here, Road no, NY 12345</li>
      </ul>
    </div>
  </section>

</body>
</html>
```